Business Card Design Project

Business Card
We are rebranding with a new logo
Industry/Entity Type
Business
Contact Information for Business Card
Dennis Marlow +61 427581962 dennis@qovo.com.au P.O. Box 872 Kelvindale QLD 4309
Requirements
Must have
- Logo

```html
<!DOCTYPE html>
<html lang="en">
<head>
<meta charset="utf-8">
<title>Qovo International – Business Card</title>
<link rel="stylesheet" href="https://fonts.googleapis.com/css2?family=Montserrat:wght@500;600;700&display=swap">
<style>
  :root {
    --page-bg: #ececec;
    --card-bg: #ffffff;
    --card-edge: #c9c9c9;
    --brand-blue: #1b86ad;
    --brand-blue-deep: #0d6a90;
    --brand-blue-light: #2a9ccb;
    --ink-teal: #1a7aa0;
    --band-text: #e6f3f8;
  }
  * { margin: 0; padding: 0; box-sizing: border-box; }
  html, body {
    width: 1200px;
    height: 1200px;
    overflow: hidden;
    background: var(--page-bg);
    font-family: "Montserrat", Arial, sans-serif;
  }
  .card {
    position: absolute;
    left: 390px;
    width: 420px;
    height: 252px;
    background: var(--card-bg);
    border: 1px solid var(--card-edge);
    overflow: hidden;
  }
  .card--front { top: 252px; }
  .card--back { top: 650px; }
  .card__band {
    position: absolute;
    inset: 0;
    width: 100%;
    height: 100%;
  }
  .brand {
    position: absolute;
    display: flex;
    align-items: center;
    gap: 8px;
    color: var(--brand-blue);
    font-weight: 700;
    letter-spacing: 0.02em;
  }
  .brand__dot {
    width: 12px;
    height: 12px;
    border-radius: 50%;
    background: var(--brand-blue);
  }
  .card--front .brand {
    top: 70px;
    left: 0;
    right: 0;
    justify-content: center;
    font-size: 26px;
  }
  .card--back .brand {
    top: 34px;
    left: 20px;
    font-size: 19px;
  }
  .card__url {
    position: absolute;
    bottom: 13px;
    left: 0;
    right: 0;
    text-align: center;
    font-size: 9px;
    font-weight: 600;
    letter-spacing: 0.32em;
    color: var(--band-text);
  }
  .contact {
    position: absolute;
    right: 20px;
    top: 118px;
    text-align: right;
    color: var(--ink-teal);
  }
  .contact__name {
    font-size: 22px;
    font-weight: 600;
    margin-bottom: 12px;
  }
  .contact__line {
    display: flex;
    justify-content: flex-end;
    align-items: center;
    gap: 6px;
    font-size: 10.5px;
    font-weight: 600;
    line-height: 16px;
  }
  .icon { width: 10px; height: 10px; }
  .card__address {
    position: absolute;
    bottom: 10px;
    left: 0;
    right: 0;
    display: flex;
    justify-content: center;
    align-items: center;
    gap: 6px;
    font-size: 10.5px;
    font-weight: 600;
    letter-spacing: 0.04em;
    color: var(--band-text);
  }
</style>
</head>
<body>

<section class="card card--front">
  <svg class="card__band" viewBox="0 0 420 252" preserveAspectRatio="none" aria-hidden="true">
    <defs>
      <linearGradient id="bandFront" x1="0" y1="0" x2="1" y2="0">
        <stop offset="0" stop-color="#0d6a90"/>
        <stop offset="0.5" stop-color="#2a9ccb"/>
        <stop offset="1" stop-color="#0d6a90"/>
      </linearGradient>
    </defs>
    <path d="M0,166 Q200,186 420,204" fill="none" stroke="#1b86ad" stroke-width="2"/>
    <path d="M0,174 Q210,206 420,204 L420,252 L0,252 Z" fill="url(#bandFront)"/>
  </svg>
  <div class="brand"><span class="brand__dot"></span>Qovo International</div>
  <p class="card__url">www.qovo.com.au</p>
</section>

<section class="card card--back">
  <svg class="card__band" viewBox="0 0 420 252" preserveAspectRatio="none" aria-hidden="true">
    <defs>
      <linearGradient id="bandBack" x1="0" y1="0" x2="1" y2="0">
        <stop offset="0" stop-color="#0d6a90"/>
        <stop offset="0.5" stop-color="#2a9ccb"/>
        <stop offset="1" stop-color="#0d6a90"/>
      </linearGradient>
    </defs>
    <path d="M0,168 Q210,180 420,212" fill="none" stroke="#1b86ad" stroke-width="2"/>
    <path d="M0,176 Q220,196 420,216 L420,252 L0,252 Z" fill="url(#bandBack)"/>
  </svg>
  <div class="brand"><span class="brand__dot"></span>Qovo International</div>

  <div class="contact">
    <p class="contact__name">Dennis Marlow</p>
    <p class="contact__line">+61 427581962
      <svg class="icon" viewBox="0 0 10 10" aria-hidden="true"><circle cx="5" cy="5" r="4.3" fill="none" stroke="#1a7aa0" stroke-width="0.9"/><path d="M3.4,2.6 L4.3,3.6 L3.9,4.2 Q4.6,5.6 5.8,6.1 L6.4,5.7 L7.3,6.6 L6.6,7.3 Q3.2,6.6 2.7,3.3 Z" fill="#1a7aa0"/></svg>
    </p>
    <p class="contact__line">dennis@qovo.com.au
      <svg class="icon" viewBox="0 0 10 10" aria-hidden="true"><circle cx="5" cy="5" r="4.3" fill="none" stroke="#1a7aa0" stroke-width="0.9"/><rect x="2.6" y="3.3" width="4.8" height="3.4" fill="none" stroke="#1a7aa0" stroke-width="0.8"/><path d="M2.6,3.3 L5,5.2 L7.4,3.3" fill="none" stroke="#1a7aa0" stroke-width="0.8"/></svg>
    </p>
  </div>

  <p class="card__address">
    <svg class="icon" viewBox="0 0 10 10" aria-hidden="true"><circle cx="5" cy="5" r="4.3" fill="none" stroke="#e6f3f8" stroke-width="0.9"/><path d="M5,2.3 A1.8,1.8 0 0 1 6.8,4.1 Q6.8,5.3 5,7.6 Q3.2,5.3 3.2,4.1 A1.8,1.8 0 0 1 5,2.3 Z" fill="#e6f3f8"/></svg>
    P.O. Box 872 Kelvindale QLD 4309
  </p>
</section>

</body>
</html>
```